1 Cup Pod - Regular and Decaf

I am looking for 2 package designs. When you open the uploaded file it show one for regular and one for decaf. The size is also on the example template. Both products with still be named Café Ordala, only things we are looking for is new colors and design of package. you can use up to 4 colors at this time.

We are open to all types of ideas and colors. the only thins is the regular and decaf must be different colors.

Requirements
Must have
• Must use the exact information used on front and back of both package design from the example template. The only thing is to add, 75702 next to where it says Tyler, TX

```html
<!DOCTYPE html>
<html lang="en">
<head>
<meta charset="utf-8">
<title>Café Ordala – Single-Cup Coffee Pod, Regular</title>
<link rel="stylesheet" href="https://fonts.googleapis.com/css2?family=Abel&display=swap">
<style>
  :root {
    --roast-dark: #230e02;
    --roast-mid: #3b1905;
    --roast-edge: #1b0a01;
    --crema-glow: #e08a0a;
    --crema-warm: #8c4808;
    --cream-text: #fbf5ee;
    --label-white: #ffffff;
    --bean-ink: #1e0e04;
  }
  * { margin: 0; padding: 0; box-sizing: border-box; }
  html, body {
    width: 1200px;
    height: 600px;
    overflow: hidden;
    background: var(--roast-dark);
  }
  .package {
    position: relative;
    width: 1200px;
    height: 600px;
    overflow: hidden;
    font-family: "Abel", "Arial Narrow", sans-serif;
    font-weight: 400;
    color: var(--cream-text);
    background:
      radial-gradient(circle at 300px 306px, var(--crema-glow) 0, var(--crema-warm) 72px, rgba(90,40,5,0.55) 190px, rgba(40,17,2,0) 330px),
      radial-gradient(circle at 900px 300px, var(--roast-mid) 0, rgba(50,22,4,0.6) 220px, rgba(30,12,1,0) 420px),
      linear-gradient(180deg, var(--roast-dark), var(--roast-edge));
  }
  .centered {
    position: absolute;
    transform: translate(-50%, -50%);
    white-space: nowrap;
    text-align: center;
    line-height: 1;
  }
  .brand-name {
    left: 300px;
    top: 220px;
    font-size: 140px;
    font-weight: 400;
    color: var(--label-white);
    text-shadow: 2px 3px 3px rgba(0,0,0,0.45);
  }
  .product-type { left: 300px; top: 362px; font-size: 23px; }
  .origin-badge { position: absolute; left: 239px; top: 392px; width: 128px; height: 52px; }
  .origin-label {
    left: 303px; top: 419px;
    font-size: 25px; font-style: italic;
    color: var(--bean-ink);
  }
  .roast-type { left: 300px; top: 493px; font-size: 33px; }
  .net-weight { left: 300px; top: 551px; font-size: 22px; }

  .directions {
    position: absolute;
    left: 900px;
    top: 166px;
    transform: translateX(-50%);
    list-style: none;
    text-align: center;
    font-size: 24px;
    line-height: 30.2px;
    white-space: nowrap;
  }
  .company-name { left: 900px; top: 455px; font-size: 29px; letter-spacing: 0.5px; }
  .company-address { left: 900px; top: 499px; font-size: 31px; }
  .company-address .zip { font-size: 23px; margin-left: 8px; }
</style>
</head>
<body>
  <main class="package">
    <section class="front-panel">
      <h1 class="brand-name centered">Café Ordala</h1>
      <p class="product-type centered">Single-Cup Coffee Pod</p>
      <svg class="origin-badge" viewBox="0 0 128 52" aria-hidden="true">
        <ellipse cx="64" cy="26" rx="63" ry="25" fill="var(--label-white)"/>
      </svg>
      <p class="origin-label centered">Colombian</p>
      <p class="roast-type centered">Regular</p>
      <p class="net-weight centered">7 g</p>
    </section>

    <section class="back-panel">
      <ul class="directions">
        <li>Directions:</li>
        <li>Carefully open package.</li>
        <li>DO NOT OPEN FILTER PACK</li>
        <li>Place single-cup coffee pod</li>
        <li>in brew basket or funnel.</li>
        <li>Follow the directions</li>
        <li>on your coffee maker.</li>
      </ul>
      <p class="company-name centered">MERIDAN &amp; SONS</p>
      <p class="company-address centered">Alder, Texas.<span class="zip">75810</span></p>
    </section>
  </main>
</body>
</html>
```